Brightwater Facility Partners Business card

We wish to have a professional Business card to present to large Corporate CEO's ASAP.

Our web site helps explain our business www.brightwaterfp.org

Brightwater Facility Partners was established after we discovered how difficult it is to organise outsourced services while heading up a business or company.

We act as a facilitator for businesses who don't have the desire, expertise or recourses to manage their own systems and meet all their requirements.

We provide an all in one facility management solution for all types of businesses. We manage schedules, contractors and costs on behalf of businesses and their needs and wants.

Having an extensive network ensures we are able to connect businesses with the right service providers.

Target Market(s)

Company CEO

Industry/Entity Type

Business

Font styles to use
Sans Serif

Colors
33a6d7
f9fdfe
0355a3

Requirements
Must have
• professional design
Nice to have
• colours to match logo

```html
<!DOCTYPE html>
<html lang="en">
<head>
<meta charset="utf-8">
<title>Brightwater Facility Partners – Business Card</title>
<link rel="stylesheet" href="https://fonts.googleapis.com/css2?family=Josefin+Slab:wght@700&family=Josefin+Sans:wght@300&family=Sorts+Mill+Goudy&display=swap">
<style>
  :root {
    --sky: #33a6d7;
    --navy: #0355a3;
    --paper: #f9fdfe;
    --white: #ffffff;
    --backdrop: #e9edf0;
    --wood-dark: #7a4e2c;
    --wood-mid: #a8774a;
    --wood-light: #cdb89a;
  }
  * { box-sizing: border-box; margin: 0; padding: 0; }
  html, body { width: 1200px; height: 750px; overflow: hidden; }
  body { background: var(--backdrop); position: relative; }

  .card {
    position: absolute;
    top: 215px;
    width: 540px;
    height: 320px;
    overflow: hidden;
    box-shadow: 0 6px 18px rgba(0,0,0,0.18);
  }
  .card--front { left: 40px; background: var(--sky); }
  .card--back { left: 620px; background: var(--paper); }

  /* Front */
  .desk-photo {
    position: absolute;
    left: 0; top: 78px;
    width: 540px; height: 200px;
    background: linear-gradient(120deg, var(--wood-light) 0%, var(--wood-mid) 35%, var(--wood-dark) 60%, var(--wood-mid) 85%, var(--wood-light) 100%);
  }
  .wave { position: absolute; left: 0; top: 0; width: 540px; height: 320px; }
  .logo-band {
    position: absolute;
    left: 28px; top: 26px;
    width: 500px; height: 134px;
    background: var(--white);
    display: flex; align-items: center; justify-content: center; gap: 16px;
  }

  /* Brand lockup */
  .brand { display: flex; align-items: center; gap: 14px; }
  .brand__dot { border-radius: 50%; background: var(--sky); flex: none; }
  .brand__name {
    font-family: "Josefin Slab", serif;
    font-weight: 700;
    color: var(--navy);
    text-align: center;
    line-height: 1.05;
  }
  .brand__line { display: block; }
  .logo-band .brand__dot { width: 46px; height: 46px; }
  .logo-band .brand__name { font-size: 31px; }
  .logo-band .brand__line--sub { font-size: 22px; letter-spacing: 7px; margin-top: 6px; }

  /* Back */
  .back-logo { position: absolute; left: 0; top: 36px; width: 540px; display: flex; justify-content: center; }
  .back-logo .brand__dot { width: 38px; height: 38px; }
  .back-logo .brand__name { font-size: 27px; }
  .back-logo .brand__line--sub { font-size: 19px; letter-spacing: 6px; margin-top: 5px; }

  .name-band {
    position: absolute;
    left: 0; top: 158px;
    width: 540px; height: 50px;
    background: var(--navy);
    display: flex; align-items: center; justify-content: center;
  }
  .holder-name {
    font-family: "Josefin Sans", sans-serif;
    font-weight: 300;
    font-size: 32px;
    letter-spacing: 5px;
    color: var(--white);
    padding-top: 4px;
  }
  .contact {
    position: absolute;
    left: 0; top: 222px;
    width: 540px;
    text-align: center;
    font-family: "Sorts Mill Goudy", serif;
    font-size: 17px;
    line-height: 27px;
    color: var(--navy);
  }
</style>
</head>
<body>
  <section class="card card--front" aria-label="Business card front">
    <div class="desk-photo" role="img" aria-label="Overhead photo of an office desk with laptop, folders, stationery and a small plant"></div>
    <svg class="wave" viewBox="0 0 540 320" aria-hidden="true">
      <path d="M0 252 C110 228 200 272 300 248 C390 226 460 214 540 232 L540 320 L0 320 Z" fill="var(--sky)"/>
    </svg>
    <div class="logo-band">
      <div class="brand">
        <span class="brand__dot"></span>
        <h1 class="brand__name">
          <span class="brand__line">BRIGHTWATER FACILITY</span>
          <span class="brand__line brand__line--sub">PARTNERS</span>
        </h1>
      </div>
    </div>
  </section>

  <section class="card card--back" aria-label="Business card back">
    <div class="back-logo">
      <div class="brand">
        <span class="brand__dot"></span>
        <h2 class="brand__name">
          <span class="brand__line">BRIGHTWATER FACILITY</span>
          <span class="brand__line brand__line--sub">PARTNERS</span>
        </h2>
      </div>
    </div>
    <div class="name-band">
      <p class="holder-name">Daniel Harcourt</p>
    </div>
    <div class="contact">
      <p>Contact: 0400 000 123</p>
      <p>Email: daniel@brightwaterfp.org</p>
    </div>
    <svg class="wave" viewBox="0 0 540 320" aria-hidden="true">
      <path d="M0 290 C90 270 170 300 270 288 C370 276 450 262 540 276 L540 320 L0 320 Z" fill="var(--navy)"/>
    </svg>
  </section>
</body>
</html>
```